Delmer's Pressure Washing Services

Starting a pressure washing business on my own in Central Valley California, not too much experience so affordable, I do houses, fences, driveways, cars, trailers, RVs. Planning to make this full-time hoping clientele picks up after having a nice business card. Design doesn't have to be flashy, more to the point, I like simplistic/personable. I do not want something exhausting to look at or with too much going on.

Target Market(s)

Residential, Commercial

Industry/Entity Type

Pressure Washing

Contact Information for Business Card

avalible Services

Font styles to use
Sans Serif

Colors
0054AA
0677BA
7BADD7
CADEEF
E8F1F8
0094D4
00A9DD
6FCCEA
C7EBF8
E9F6FB
00AB8E
00BBA5
67D7C9
C6EFE9
E9F9F6

```html
<!DOCTYPE html>
<html lang="en">
<head>
<meta charset="utf-8">
<title>Delmer's Pressure Washing Services – Business Card</title>
<link href="https://fonts.googleapis.com/css2?family=Exo+2:wght@400;500;700&display=swap" rel="stylesheet">
<style>
  :root {
    --navy: #223a67;
    --ink: #1c1c1c;
    --paper: #ffffff;
    --stage: #e4e5e7;
    --brand-blue: #0054AA;
    --divider: #223a67;
  }
  * { box-sizing: border-box; margin: 0; padding: 0; }
  html, body {
    width: 950px; height: 1200px; overflow: hidden;
    background: var(--stage);
    font-family: "Exo 2", Arial, sans-serif;
  }
  .canvas { position: relative; width: 950px; height: 1200px; }
  .card {
    position: absolute; left: 125px; width: 700px; height: 400px;
    box-shadow: 0 6px 18px rgba(0,0,0,.12);
  }
  .card--front { top: 150px; background: var(--navy); }
  .card--back { top: 650px; background: var(--paper); }

  /* front */
  .logo-panel {
    position: absolute; left: 100px; top: 125px; width: 500px; height: 150px;
    background: var(--paper);
    display: flex; align-items: center; justify-content: center; gap: 26px;
  }
  .wordmark {
    display: flex; align-items: center; gap: 12px;
    font-weight: 700; font-size: 52px; color: var(--brand-blue); line-height: 1;
  }
  .wordmark__square { width: 22px; height: 22px; background: currentColor; }
  .tagline {
    font-weight: 500; font-size: 20px; line-height: 1.1; letter-spacing: .5px;
    color: var(--ink); text-transform: uppercase;
  }

  /* back */
  .identity {
    position: absolute; left: 0; top: 0; width: 100%; height: 280px;
    display: flex; align-items: center; padding-left: 70px;
  }
  .identity__name { width: 290px; }
  .name { font-weight: 700; font-size: 40px; color: var(--ink); line-height: 1; }
  .role { font-size: 14px; color: var(--ink); text-align: right; margin-top: 4px; padding-right: 20px; }
  .identity__divider { width: 2px; height: 120px; background: var(--divider); margin: 0 26px 0 10px; }
  .contact { font-weight: 500; font-size: 20px; color: var(--ink); line-height: 1.25; }
  .band {
    position: absolute; left: 0; bottom: 0; width: 100%; height: 120px;
    background: var(--navy);
    display: flex; align-items: center; justify-content: center; gap: 20px;
  }
  .band .wordmark { color: var(--paper); font-size: 40px; gap: 10px; }
  .band .wordmark__square { width: 16px; height: 16px; }
  .band .tagline { color: var(--paper); font-size: 15px; font-weight: 400; }
</style>
</head>
<body>
<main class="canvas">
  <section class="card card--front" aria-label="Card front">
    <div class="logo-panel">
      <div class="wordmark"><span class="wordmark__square"></span>Delmer's</div>
      <p class="tagline">Pressure<br>Washing<br>Services</p>
    </div>
  </section>

  <section class="card card--back" aria-label="Card back">
    <div class="identity">
      <div class="identity__name">
        <p class="name">Delmer Ruiz</p>
        <p class="role">C.E.O</p>
      </div>
      <span class="identity__divider"></span>
      <div class="contact">
        <p>2095550142</p>
        <p>info@delmerswash.com</p>
      </div>
    </div>
    <div class="band">
      <div class="wordmark"><span class="wordmark__square"></span>Delmer's</div>
      <p class="tagline">Pressure<br>Washing<br>Services</p>
    </div>
  </section>
</main>
</body>
</html>
```